Meridian Umbrella - Application form

I have an old application form in an editable PDF format (attached) which needs updating and bringing into the new branding. I would like both a word and editable PDF version of the application form

Target Market(s)

Contractors who are looking to join and use our umbrella services

Requirements
Must have
• All fields in the attached PDF version.
• Inline with the look and feel of the logo and web design attached.

```html
<!DOCTYPE html>
<html lang="en">
<head>
<meta charset="utf-8">
<title>Meridian Umbrella – Application Form</title>
<link href="https://fonts.googleapis.com/css2?family=Mulish:wght@400;700&display=swap" rel="stylesheet">
<style>
  :root {
    --backdrop: #efefef;
    --paper: #ffffff;
    --ink: #1a1a1a;
    --ink-soft: #3a3a3a;
    --field: #ebebeb;
    --field-edge: #c9c9c9;
  }
  * { box-sizing: border-box; margin: 0; padding: 0; }
  html, body {
    width: 1200px; height: 814px; overflow: hidden;
    background: var(--backdrop);
    font-family: "Mulish", sans-serif;
    color: var(--ink);
  }
  .form-page {
    position: absolute; left: 310px; top: 17px;
    width: 580px; height: 780px;
    background: var(--paper);
    box-shadow: 0 2px 10px rgba(0,0,0,0.08);
    padding: 34px 40px 30px;
  }
  .masthead { display: flex; align-items: center; gap: 34px; }
  .brand { display: flex; align-items: center; gap: 8px; }
  .brand-square { width: 18px; height: 18px; background: var(--ink); flex: none; }
  .brand-name { font-size: 13px; font-weight: 700; letter-spacing: 0.5px; line-height: 1.15; width: 80px; }
  .form-title {
    font-size: 20px; font-weight: 700; letter-spacing: 4px;
    padding-bottom: 5px; position: relative;
  }
  .form-title::after {
    content: ""; position: absolute; left: 38%; width: 24%; bottom: 0;
    border-bottom: 1.5px solid var(--ink);
  }
  .intro { font-size: 10px; line-height: 1.4; margin: 16px 0 14px; color: var(--ink-soft); }
  .section-heading {
    font-size: 12.5px; font-weight: 700; text-decoration: underline;
    text-align: center; margin: 12px 0 12px;
  }
  .row { display: flex; align-items: center; gap: 10px; margin-bottom: 9px; font-size: 10.5px; }
  .pair { display: flex; align-items: center; gap: 6px; flex: 1; min-width: 0; }
  .pair label { white-space: nowrap; }
  .field { flex: 1; height: 14px; background: var(--field); border: 1px solid var(--field-edge); }
  .tick { width: 11px; height: 11px; border: 1px solid var(--field-edge); background: var(--field); flex: none; }
  .title-options { display: flex; align-items: center; gap: 6px; }
  .title-options .other { width: 70px; flex: none; }
  .area { height: 64px; background: var(--field); border: 1px solid var(--field-edge); margin: 6px 0 16px; }
  .prose { font-size: 10.5px; line-height: 1.4; }
  .categories { display: grid; grid-template-columns: 1fr 1fr; gap: 8px 12px; margin: 8px 0 12px; font-size: 10.5px; }
  .categories .wide { grid-column: 1 / -1; }
  .category { display: flex; align-items: center; gap: 6px; }
</style>
</head>
<body>
  <main class="form-page">
    <header class="masthead">
      <div class="brand">
        <span class="brand-square"></span>
        <span class="brand-name">Meridian Umbrella</span>
      </div>
      <h1 class="form-title">Application Form</h1>
    </header>

    <p class="intro">Please complete the form below and detail your permanent residential information as per your identification documentation. We'll start processing your application straight away.</p>

    <h2 class="section-heading">Applicant and Permanent Residential Information</h2>

    <div class="row">
      <label>Title (as per identification documents):</label>
      <div class="title-options">
        <span>Mr:</span><span class="tick"></span>
        <span>Mrs:</span><span class="tick"></span>
        <span>Miss:</span><span class="tick"></span>
        <span>Ms:</span><span class="tick"></span>
        <span>Other:</span><span class="field other"></span>
      </div>
    </div>
    <div class="row">
      <div class="pair"><label>Forename(s):</label><span class="field"></span></div>
      <div class="pair"><label>Surname:</label><span class="field"></span></div>
    </div>
    <div class="row">
      <div class="pair"><label>Are you a UK resident for tax purposes?</label><span class="field"></span></div>
      <div class="pair"><label>Mobile Telephone:</label><span class="field"></span></div>
    </div>
    <div class="row">
      <div class="pair"><label>Home Telephone:</label><span class="field"></span></div>
      <div class="pair"><label>House Name/Number:</label><span class="field"></span></div>
    </div>
    <div class="row">
      <div class="pair"><label>Email Address:</label><span class="field"></span></div>
      <div class="pair"></div>
    </div>
    <div class="row">
      <div class="pair"><label>Street/Road Name:</label><span class="field"></span></div>
      <div class="pair"><label>Country:</label><span class="field"></span></div>
    </div>
    <div class="row">
      <div class="pair"><label>Town/City:</label><span class="field"></span></div>
      <div class="pair"><label>Nationality:</label><span class="field"></span></div>
    </div>
    <div class="row">
      <div class="pair"><label>Postcode:</label><span class="field"></span></div>
      <div class="pair"><label>Your NI Number:</label><span class="field"></span></div>
    </div>
    <div class="row">
      <div class="pair"><label>Date of Birth:</label><span class="field"></span></div>
      <div class="pair"></div>
    </div>

    <h2 class="section-heading">About Your Work</h2>

    <div class="row">
      <div class="pair"><label>Industry Sector:</label><span class="field"></span></div>
      <div class="pair"><label>Job Title:</label><span class="field"></span></div>
    </div>
    <p class="prose">Please tick which category best describes your role:</p>
    <div class="categories">
      <div class="category"><span class="tick"></span>Clerical - Administrative/IT</div>
      <div class="category"><span class="tick"></span>Clerical - Technical/Professional</div>
      <div class="category wide"><span class="tick"></span>Manual (NB: this means your role involves use of hand tools more than 20% of the time)</div>
    </div>
    <p class="prose">Short description of key responsibilities (e.g. "I am responsible for designing, developing and executing test plans"):</p>
    <div class="area"></div>
    <p class="prose">Please list any qualifications, authorisations, experience or training requirements placed upon you by your end client, agency or professional body to undertake your role:</p>
    <div class="area"></div>
    <p class="prose">I confirm that I have all of the above and will co-operate in any checks in relation to these as required. Does your role require you to have regular access to vulnerable adults and/or young children?</p>
  </main>
</body>
</html>
```